Corporate Web Redesign Project - coded

We would like redesign/refresh of our current site that would allow us to increase the depth of content and create a high quality impression for visitors.

Current site - http://corvanisystems.example/

A previous web redesign project has improved our site but it has not really reached the level we require.

Our customers are global, blue chip, organisations and a professional, corporate style of site is required.

Please note we would prefer a coded website to a just a design. We are happy to provide a zip of our current site if required.
Updates

                                   

Target Market(s)

Global oil and gas producers, KT, Pardo, Valmira etc.

Industry/Entity Type

It Professional

Requirements
Must have
• Design should support the level of content we currently have in the existing sitemap - although it should be expandable a site design for a large / complex site would not be appropriate

All current content / pages to be reflected in design

Must be visually appealing

Intuitive and clear navigation that is expandable

Display a high level of professionalism

Use a consistent palette of colours that complements our logo

Clean and organized layout

A way to capture visitor’s information or Call to action (i.e. contact link or form) on every page

Prominent Contact Information
Should not have
• Flash

```html
<!DOCTYPE html>
<html lang="en">
<head>
<meta charset="utf-8">
<title>Corvani Systems</title>
<link href="https://fonts.googleapis.com/css2?family=Roboto:wght@300;400;500;700&display=swap" rel="stylesheet">
<style>
:root{
  --teal:#2d6170;
  --teal-dark:#1f4b5a;
  --teal-light:#5e9aa6;
  --ink:#1d4756;
  --grey:#9a9a9a;
  --grey-light:#c4c4c4;
  --white:#ffffff;
  --footer-bg:#fafafa;
}
*{margin:0;padding:0;box-sizing:border-box}
html,body{width:771px;height:1200px;overflow:hidden;background:var(--white);font-family:'Roboto',sans-serif}
.page{position:relative;width:771px;height:1200px}
.topbar{position:absolute;top:0;left:0;width:771px;height:6px;display:flex}
.topbar span:nth-child(1){flex:0 0 243px;background:var(--teal-dark)}
.topbar span:nth-child(2){flex:0 0 285px;background:var(--teal)}
.topbar span:nth-child(3){flex:1;background:var(--teal-light)}
.brand{position:absolute;left:128px;top:40px;display:flex;align-items:center;gap:8px;color:var(--ink);font-weight:700;font-size:15px;letter-spacing:.5px}
.brand i{width:22px;height:22px;border-radius:50%;background:var(--teal);display:block}
.nav{position:absolute;top:51px;left:323px;display:flex;gap:19px;font-size:12.5px;color:var(--grey);font-weight:500}
.nav .active{color:var(--ink)}
.hero-art{position:absolute;left:120px;top:96px;width:300px;height:184px;background:radial-gradient(ellipse at 50% 50%,#e3e6e7 0%,#f2f3f3 55%,#fff 100%)}
.hero-title{position:absolute;left:385px;top:126px;font-size:15.5px;font-weight:300;letter-spacing:1.3px;color:var(--ink)}
.ticks{position:absolute;left:385px;top:158px;list-style:none}
.ticks li{display:flex;align-items:center;gap:6px;height:21.5px;font-size:11.3px;font-weight:500;color:var(--ink)}
.welcome{position:absolute;top:298px;left:0;width:771px;text-align:center}
.welcome h1{font-size:12px;font-weight:500;letter-spacing:1.8px;color:var(--ink)}
.welcome p{margin:10px auto 0;width:530px;font-size:8.4px;line-height:17px;color:var(--grey);font-weight:300}
.band{position:absolute;top:410px;left:0;width:771px;height:502px;background:var(--teal)}
.service{position:absolute;left:91px;width:300px;color:var(--white)}
.service h2{font-size:15px;font-weight:300;letter-spacing:1.2px}
.service p{margin-top:5px;width:160px;font-size:8.7px;line-height:17px;font-weight:400}
.service svg{position:absolute;left:180px;top:40px}
.news{position:absolute;left:393px;top:428px;width:271px;height:448px;background:var(--white);padding:6px 12px}
.news h3{font-size:15px;font-weight:300;color:var(--teal);letter-spacing:.6px;margin-top:6px}
.news p{font-size:7px;line-height:15px;color:var(--grey);margin-top:4px}
.news .item{margin-bottom:16px}
.clients{position:absolute;top:975px;left:110px;display:flex;gap:30px;align-items:center}
.client{font-size:10px;color:var(--grey-light);font-weight:500;display:flex;align-items:center;gap:4px}
.client b{width:14px;height:14px;background:#d6d6d6;display:block}
.foot{position:absolute;top:1045px;font-size:7px;line-height:17.5px;color:var(--grey);letter-spacing:.3px}
.foot strong{font-weight:700}
.foot-brand{position:absolute;left:128px;top:1076px;display:flex;align-items:center;gap:6px;color:#c0d2d6;font-weight:700;font-size:11px}
.foot-brand i{width:16px;height:16px;border-radius:50%;background:#cfdfe2;display:block}
</style>
</head>
<body>
<div class="page">
  <div class="topbar"><span></span><span></span><span></span></div>
  <div class="brand"><i></i>CORVANI SYSTEMS</div>
  <nav class="nav"><span class="active">Home</span><span>News</span><span>About Us</span><span>Solutions</span><span>Contact Us</span></nav>

  <div class="hero-art" role="img" aria-label="Faint illustration of a drilling rig and equipment"></div>
  <div class="hero-title">THE BUSINESS OF DRILLING WELLS</div>
  <ul class="ticks">
    <li><svg width="15" height="15" viewBox="0 0 16 16"><circle cx="8" cy="8" r="7" fill="none" stroke="#1d4756" stroke-width="1.4"/><path d="M4.5 8.2l2.3 2.3 4.7-4.8" fill="none" stroke="#1d4756" stroke-width="1.5"/></svg>Understand and communicate project cost and risk</li>
    <li><svg width="15" height="15" viewBox="0 0 16 16"><circle cx="8" cy="8" r="7" fill="none" stroke="#1d4756" stroke-width="1.4"/><path d="M4.5 8.2l2.3 2.3 4.7-4.8" fill="none" stroke="#1d4756" stroke-width="1.5"/></svg>Control and reduce expenditure</li>
    <li><svg width="15" height="15" viewBox="0 0 16 16"><circle cx="8" cy="8" r="7" fill="none" stroke="#1d4756" stroke-width="1.4"/><path d="M4.5 8.2l2.3 2.3 4.7-4.8" fill="none" stroke="#1d4756" stroke-width="1.5"/></svg>Learn and improve performance</li>
  </ul>

  <section class="welcome">
    <h1>Welcome to Corvani Systems Ltd</h1>
    <p>For more than a decade Corvani Systems has been helping companies better manage the Business of Drilling Wells.<br>
    We are an integrated software and consulting organization, helping companies across the globe to understand, mitigate and communicate risk, control cost and deliver performance improvement. Our systems are in use in over 30 countries with a broad range of clients including: Tessaro, KT, Valmira, Northquay, Halden, Marlow and Ravel</p>
  </section>

  <section class="band">
    <div class="service" style="top:26px">
      <h2>TIME &amp; COST ESTIMATION</h2>
      <p>RPX delivers a standardized, systematic approach to understanding project risk.</p>
      <svg width="24" height="26" viewBox="0 0 24 26"><circle cx="12" cy="15" r="9" fill="none" stroke="#fff" stroke-width="2.2"/><rect x="9.5" y="1.5" width="5" height="3" fill="#fff"/><path d="M12 15V9" stroke="#fff" stroke-width="2"/></svg>
    </div>
    <div class="service" style="top:142px">
      <h2>MATERIALS &amp; COST CONTROL</h2>
      <p>CMX has been helping companies optimize materials and cost tracking processes since 1992.</p>
      <svg width="24" height="24" viewBox="0 0 24 24"><path d="M12 2l5 8h-10z M3 20l4-8 4 8z M21 20l-4-8-4 8z" fill="#fff"/></svg>
    </div>
    <div class="service" style="top:256px">
      <h2>LESSONS LEARNED</h2>
      <p>LKX is an advanced lessons learned &amp; knowledge system for use in the energy industry</p>
      <svg width="26" height="22" viewBox="0 0 26 22"><path d="M3 15l12-12 8 6-12 12z" fill="#fff"/><path d="M3 15l8 6" stroke="#fff" stroke-width="2"/></svg>
    </div>
    <div class="service" style="top:379px">
      <h2>SERVICES &amp; CONSULTING</h2>
      <p>Successful software implementations rely on people and processes to deliver results</p>
      <svg width="24" height="24" viewBox="0 0 24 24" style="top:50px"><path d="M4 4l16 16M20 4L4 20" stroke="#fff" stroke-width="3" stroke-linecap="round"/></svg>
    </div>
  </section>

  <aside class="news">
    <div class="item">
      <h3>LATEST NEWS</h3>
      <p>RPX Selected by Marlow<br>Marlow Energy Ltd has selected RPX as the solution to provide probabilistic time and cost estimates for its drilling operations.</p>
    </div>
    <div class="item">
      <h3>CMX Implementation at Northquay</h3>
      <p>Northquay selects CMX to support its materials, logistics &amp; cost management processes</p>
    </div>
    <div class="item">
      <h3>RPX Selected by Marlow</h3>
      <p>Marlow Energy Ltd has selected RPX as the solution to provide probabilistic time and cost estimates for its drilling operations.</p>
    </div>
  </aside>

  <div class="clients">
    <span class="client"><b></b>Valmira</span>
    <span class="client"><b></b>Ravel</span>
    <span class="client">Tessaro</span>
    <span class="client">Marlow</span>
    <span class="client"><b></b>KT</span>
    <span class="client">Northquay</span>
    <span class="client">Halden</span>
  </div>

  <div class="foot" style="left:119px">Copyright © Corvani Systems Ltd 2013</div>
  <div class="foot-brand"><i></i>CORVANI SYSTEMS</div>
  <div class="foot" style="left:271px"><strong>EUROPE</strong><br>12 Harlaw Row<br>Aberdeen<br>AB10 1ZZ<br>Phone:+44(0)1224 000 100<br>Email: eu@corvanisystems.example<br>NORTH AMERICA</div>
  <div class="foot" style="left:405px"><strong>NORTH AMERICA</strong><br>1800 Westline Drive<br>Suite 210<br>Houston, TX 77000<br>Phone:(713) 555 0142<br>Email: us@corvanisystems.example</div>
</div>
</body>
</html>
```